Bodywork Quietude Business Card Design

I want to create a very elegant and sophisticated two sided business card for my massage practice (www.bodyworkquietude.net). I have attached the logo and a PDF with some ideas down for the back of the card but I am open to suggestions. I will want to tie in a post card and flyer to the card later.
Similar colors to website would be great.
Target Market(s)
High end clientele, people looking for a sophisticated spa experience.
Industry/Entity Type
Massage
Contact Information for Business Card
Bodywork Quietude
7318 Larkspur Ave S, Suite 305
Seattle, WA 98103
(206) 555-0147
www.bodyworkquietude.net
Look and feel

```html
<!DOCTYPE html>
<html lang="en">
<head>
<meta charset="utf-8">
<title>Bodywork Quietude — Business Card</title>
<link rel="stylesheet" href="https://fonts.googleapis.com/css2?family=Arimo:wght@400;700&display=swap">
<style>
  :root {
    --stage: #000000;
    --card: #ffffff;
    --navy: #1d3645;
    --sand: #d5cec4;
    --ink: #1d3645;
    --ink-soft: #2b3a44;
  }
  html, body {
    margin: 0;
    padding: 0;
    width: 1200px;
    height: 751px;
    overflow: hidden;
    background: var(--stage);
    font-family: "Arimo", Arial, sans-serif;
  }
  .canvas {
    position: relative;
    width: 1200px;
    height: 751px;
  }
  .card {
    position: absolute;
    top: 215px;
    width: 561px;
    height: 322px;
    background: var(--card);
    overflow: hidden;
  }
  .card--front { left: 19px; }
  .card--back { left: 621px; }

  .band-navy {
    position: absolute;
    left: 0; right: 0;
    top: 293px;
    height: 7px;
    background: var(--navy);
  }
  .band-sand {
    position: absolute;
    left: 0; right: 0;
    top: 301px;
    height: 21px;
    background: var(--sand);
  }

  .brand-mark {
    position: absolute;
    color: var(--ink);
    font-weight: 400;
    text-transform: uppercase;
    white-space: nowrap;
    transform: translate(-50%, -50%);
  }
  .card--front .brand-mark {
    left: 132px;
    top: 80px;
    font-size: 17px;
    letter-spacing: 1px;
  }
  .card--back .brand-mark {
    left: 280px;
    top: 150px;
    font-size: 30px;
    letter-spacing: 2px;
  }

  .business-name {
    position: absolute;
    left: 325px;
    top: 98px;
    margin: 0;
    font-size: 18.5px;
    font-weight: 700;
    color: var(--ink);
  }
  .contact {
    position: absolute;
    right: 16px;
    top: 180px;
    margin: 0;
    padding: 0;
    list-style: none;
    text-align: right;
    font-size: 12.5px;
    color: var(--ink-soft);
  }
  .contact li {
    height: 24.5px;
    line-height: 16px;
  }
</style>
</head>
<body>
<main class="canvas">
  <section class="card card--front" aria-label="Card front">
    <div class="brand-mark">Bodywork Quietude</div>
    <h1 class="business-name">Bodywork Quietude</h1>
    <ul class="contact">
      <li class="contact-phone">(206) 555-0147</li>
      <li class="contact-web">www.bodyworkquietude.net</li>
      <li class="contact-address">7318 Larkspur Ave S, Suite 305, Seattle, WA 98103</li>
    </ul>
    <div class="band-navy"></div>
    <div class="band-sand"></div>
  </section>

  <section class="card card--back" aria-label="Card back">
    <div class="brand-mark">Bodywork Quietude</div>
    <div class="band-navy"></div>
    <div class="band-sand"></div>
  </section>
</main>
</body>
</html>
```